i would like a business card to leave with customers and potential customers for electrical work and for the supply and install of reverse cycle airconditioning in the domestic and commercial market.
I own my own business and im a sole trader. I have an a'class electrical lisence and also a refrigeration lisence so i am
able to offer complete installations in airconditioning by a fully qualified and lisenced tradesman.
im looking for something that comes across as unique and professional.
i had the coluor black and some gold in mind but open to any coluors.
something like Beacon Electrical & Refrigeration
or Beacon Air.
i will use this design on a business card to advertise through summer to help generate installs through the busy season.

Target Market(s)

Mainly domestic house holds through summer who are in need of airconditioning and reliable information to acomadate thier cooling and heating requirements

Industry/Entity Type

Electrical

Requirements
Must have
• Business name- Beacon
My name- Peter Wollaston
My mobile no- 0457 819 302
My email- prwollaston@tarvel.com.au
Installation & Decomissioning of aiconditioning split systems
LIC NO: KTR 407516
Nice to have
• Beacon Electrical & Refrigeration

```html
<!DOCTYPE html>
<html lang="en">
<head>
<meta charset="utf-8">
<title>Beacon Electrical &amp; Refrigeration – Business Card</title>
<link rel="stylesheet" href="https://fonts.googleapis.com/css2?family=Arimo:wght@400;700&family=Tinos&display=swap">
<style>
  :root {
    --stage: #e4e4e4;
    --ink: #000000;
    --paper: #ffffff;
    --gold: #c9a219;
    --label: #111111;
    --text-font: "Arimo", Arial, sans-serif;
    --label-font: "Tinos", "Times New Roman", serif;
  }
  * { margin: 0; padding: 0; box-sizing: border-box; }
  html, body { width: 1200px; height: 900px; overflow: hidden; }
  body { position: relative; background: var(--stage); font-family: var(--text-font); }

  .side-label {
    position: absolute;
    font-family: var(--label-font);
    font-size: 26px;
    color: var(--label);
    letter-spacing: 0.5px;
  }
  .side-label--front { left: 931px; top: 128px; }
  .side-label--back { left: 184px; top: 713px; }

  .card { position: absolute; width: 499px; height: 283px; overflow: hidden; }

  /* Front */
  .card--front { left: 520px; top: 168px; background: var(--paper); }
  .front-band {
    position: absolute; top: 67px; height: 150px; background: var(--ink);
  }
  .front-band--tagline { left: 0; width: 151px; border-radius: 0 18px 18px 0; }
  .front-band--brand { left: 162px; width: 337px; border-radius: 18px 0 0 18px; }
  .tagline {
    position: absolute; right: 17px; top: 42px;
    text-align: right; color: var(--gold);
    font-size: 13px; line-height: 17px;
  }

  .wordmark { position: absolute; display: flex; align-items: center; color: var(--gold); }
  .wordmark__name { font-weight: 400; line-height: 1; }
  .wordmark__divider { background: var(--gold); width: 1px; }
  .wordmark__trade { font-weight: 400; }

  .card--front .wordmark { left: 25px; top: 48px; }
  .card--front .wordmark__name { font-size: 34px; margin-right: 11px; }
  .card--front .wordmark__divider { height: 59px; margin-right: 10px; }
  .card--front .wordmark__trade { font-size: 19px; line-height: 25px; }

  /* Back */
  .card--back { left: 173px; top: 418px; background: var(--ink); width: 498px; }
  .back-tab { position: absolute; top: 67px; width: 50px; height: 150px; background: var(--paper); }
  .back-tab--left { left: 0; }
  .back-tab--right { right: 0; }

  .card--back .wordmark { left: 75px; top: 82px; }
  .card--back .wordmark__name { font-size: 23px; margin-right: 8px; }
  .card--back .wordmark__divider { height: 41px; margin-right: 7px; }
  .card--back .wordmark__trade { font-size: 14px; line-height: 17px; }

  .contact { position: absolute; left: 73px; top: 145px; color: var(--paper); }
  .contact__name { font-weight: 700; font-size: 15px; margin-bottom: 5px; }
  .contact__line { display: flex; align-items: center; font-size: 13px; line-height: 17px; }
  .contact__icon { width: 11px; height: 11px; margin-right: 5px; flex: none; }

  .licence {
    position: absolute; right: 101px; top: 168px;
    text-align: right; color: var(--paper);
    font-size: 8px; line-height: 11px;
  }
  .authorised-badge { position: absolute; left: 397px; top: 157px; width: 32px; height: 35px; background: var(--gold); }
</style>
</head>
<body>
  <div class="side-label side-label--front">FRONT</div>

  <section class="card card--front" aria-label="Card front">
    <div class="front-band front-band--tagline">
      <p class="tagline">Installation and<br>Decomissioning of<br>Air Conditioning<br>Split Systems</p>
    </div>
    <div class="front-band front-band--brand">
      <div class="wordmark">
        <span class="wordmark__name">Beacon</span>
        <span class="wordmark__divider"></span>
        <span class="wordmark__trade">Electrical &amp;<br>Refrigeration</span>
      </div>
    </div>
  </section>

  <section class="card card--back" aria-label="Card back">
    <div class="back-tab back-tab--left"></div>
    <div class="back-tab back-tab--right"></div>

    <div class="wordmark">
      <span class="wordmark__name">Beacon</span>
      <span class="wordmark__divider"></span>
      <span class="wordmark__trade">Electrical &amp;<br>Refrigeration</span>
    </div>

    <div class="contact">
      <p class="contact__name">Peter Wollaston</p>
      <p class="contact__line">
        <svg class="contact__icon" viewBox="0 0 11 11" aria-hidden="true">
          <rect x="2.5" y="0.5" width="6" height="10" rx="1" fill="none" stroke="#c9a219" stroke-width="1"/>
          <rect x="3.7" y="2" width="3.6" height="4.5" fill="#c9a219"/>
        </svg>0457 819 302
      </p>
      <p class="contact__line">
        <svg class="contact__icon" viewBox="0 0 11 11" aria-hidden="true">
          <rect x="0.5" y="2" width="10" height="7" fill="none" stroke="#c9a219" stroke-width="1"/>
          <polyline points="0.5,2 5.5,6 10.5,2" fill="none" stroke="#c9a219" stroke-width="1"/>
        </svg>prwollaston@tarvel.com.au
      </p>
    </div>

    <p class="licence">LIC NO:<br>KTR 407516</p>
    <div class="authorised-badge" role="img" aria-label="Authorised licence badge"></div>
  </section>

  <div class="side-label side-label--back">BACK</div>
</body>
</html>
```